Detail Shop Business card design

i need a business card design for my new detailing company called 'Brenner's Detail Shop'. i want an all black and white design . simple, direct and to the point. i want the designer to choose a fitting font to match the logothe front should have logo, address, phone and email and the back side should have a slogan and text indicating that we offer services on anything including cars, trucks, motorcycles and RVs. slogan will read "we take pride in your ride"
maybe also very small on the back side the IG icon with Brenners_Detail_Shop

phone 482.615.7734
address 7384 E Harlow Ave
Spokane WA 99342
email: BrennersDetail@quorvail.com

Target Market(s)

all ages , auto enthusiasts

Industry/Entity Type

Automotive

Contact Information for Business Card

the front should have logo, address, phone and email and the back side should have a slogan and text indicating that we offer services on anything including cars, trucks, motorcycles and RVs. slogan will read "we take pride in your ride"

phone 482.615.7734
address 7384 E Harlow Ave
Spokane WA 99342

Colors
000000
ffffff

Requirements
Must have
• bold font and very simple design with good spacing
Nice to have
• anything creative from the designer indicating we service any types of vehicles
Should not have
• any colors ,

```html
<!DOCTYPE html>
<html lang="en">
<head>
<meta charset="utf-8">
<title>Brenner's Detail Shop – Business Card</title>
<link rel="stylesheet" href="https://fonts.googleapis.com/css2?family=Lato:wght@400;900&family=Lobster+Two:ital,wght@1,400&display=swap">
<style>
  :root {
    --ink: #000000;
    --paper: #ffffff;
    --stage: #d9d9d9;
    --soft-ink: #1a1a1a;
    --faint: rgba(255,255,255,0.06);
  }
  * { box-sizing: border-box; margin: 0; padding: 0; }
  html, body { width: 1200px; height: 782px; overflow: hidden; }
  body {
    background: var(--stage);
    font-family: "Lato", Arial, sans-serif;
    position: relative;
  }
  .card {
    position: absolute;
    top: 236px;
    width: 540px;
    height: 309px;
    overflow: hidden;
    box-shadow: 0 6px 18px rgba(0,0,0,0.25);
  }

  /* Back side */
  .card-back { left: 40px; background: var(--ink); }
  .slogan-band {
    position: absolute; left: 0; top: 0; bottom: 0; width: 78px;
    background: var(--paper);
  }
  .slogan {
    position: absolute; left: 39px; top: 154px;
    transform: translate(-50%, -50%) rotate(-90deg);
    white-space: nowrap;
    font-size: 15px; letter-spacing: 0.5px;
    color: var(--ink);
  }
  .services {
    position: absolute; left: 150px; top: 70px; width: 330px;
    font-family: "Lobster Two", "Brush Script MT", cursive;
    font-style: italic;
    font-size: 26px; line-height: 1.3;
    color: var(--paper);
  }
  .back-emblem {
    position: absolute; right: -60px; bottom: -70px;
    width: 260px; height: 260px; border-radius: 50%;
    background: var(--faint);
  }

  /* Front side */
  .card-front { left: 620px; background: var(--paper); }
  .front-band { position: absolute; left: 0; top: 0; width: 120px; height: 309px; }
  .contact-list { position: absolute; left: 40px; top: 44px; list-style: none; }
  .contact-item {
    display: flex; align-items: flex-start; gap: 10px;
    margin-bottom: 16px;
    font-size: 17px; line-height: 1.15; color: var(--soft-ink);
  }
  .contact-icon {
    flex: none; width: 30px; height: 30px; border-radius: 50%;
    background: var(--paper); border: 2px solid var(--ink);
    display: flex; align-items: center; justify-content: center;
  }
  .contact-text { padding-top: 5px; }
  .brand {
    position: absolute; right: 34px; bottom: 46px;
    display: flex; flex-direction: column; align-items: center; gap: 10px;
  }
  .brand-mark { width: 70px; height: 70px; border-radius: 50%; background: var(--ink); }
  .brand-name {
    font-family: "Lato", Arial, sans-serif; font-weight: 900;
    font-size: 22px; color: var(--ink); text-align: center; line-height: 1.1;
    width: 180px;
  }
</style>
</head>
<body>

<section class="card card-back" aria-label="Card back">
  <div class="slogan-band"><p class="slogan">WE TAKE PRIDE IN YOUR RIDE</p></div>
  <div class="back-emblem" aria-hidden="true"></div>
  <p class="services">We offer services on anything including cars, trucks, motorcycles and RVs.</p>
</section>

<section class="card card-front" aria-label="Card front">
  <svg class="front-band" viewBox="0 0 120 309" aria-hidden="true">
    <path d="M0 0 H95 Q40 150 60 309 H0 Z" fill="#000"/>
  </svg>
  <ul class="contact-list">
    <li class="contact-item">
      <span class="contact-icon">
        <svg width="14" height="14" viewBox="0 0 24 24"><path d="M6.6 10.8a15 15 0 0 0 6.6 6.6l2.2-2.2c.3-.3.7-.4 1-.2 1.1.4 2.3.6 3.6.6.6 0 1 .4 1 1V20c0 .6-.4 1-1 1A17 17 0 0 1 3 4c0-.6.4-1 1-1h3.5c.6 0 1 .4 1 1 0 1.3.2 2.5.6 3.6.1.3 0 .7-.2 1z" fill="#000"/></svg>
      </span>
      <span class="contact-text">482.615.7734</span>
    </li>
    <li class="contact-item">
      <span class="contact-icon">
        <svg width="14" height="14" viewBox="0 0 24 24"><rect x="2" y="5" width="20" height="14" rx="1.5" fill="#000"/><path d="M3 6l9 7 9-7" stroke="#fff" stroke-width="1.6" fill="none"/></svg>
      </span>
      <span class="contact-text">BrennersDetail@quorvail.com</span>
    </li>
    <li class="contact-item">
      <span class="contact-icon">
        <svg width="14" height="14" viewBox="0 0 24 24"><path d="M12 2a7 7 0 0 0-7 7c0 5 7 13 7 13s7-8 7-13a7 7 0 0 0-7-7zm0 9.5a2.5 2.5 0 1 1 0-5 2.5 2.5 0 0 1 0 5z" fill="#000"/></svg>
      </span>
      <span class="contact-text">7384 E Harlow Ave<br>Spokane WA 99342</span>
    </li>
    <li class="contact-item">
      <span class="contact-icon" aria-hidden="true"></span>
      <span class="contact-text">Brenners_Detail_Shop</span>
    </li>
  </ul>
  <div class="brand">
    <div class="brand-mark" aria-hidden="true"></div>
    <p class="brand-name">Brenner's Detail Shop</p>
  </div>
</section>

</body>
</html>
```